BRISK FLOW HEATING AND COOLING WORKING VAN

I'm in heating and cooling business and i want something something eye-catching. With my phone number 416-502-3964 and website brisk-flow.ca
I was also thinking to add some funny character but not necessary

2020 ford transit high roof extended- white

Font styles to use
Serif
Decorative
Script

Colors
0456a4
ec1f27
33a6d7
00a990
f68d4d
f78f20
85cae6
acd037
f37122

Requirements
Must have
• MY LOGO
PHONE NUMBER 416-502-3964
MY WEBSITE BRISK-FLOW.CA

```html
<!DOCTYPE html>
<html lang="en">
<head>
<meta charset="utf-8">
<title>Brisk Flow Heating and Cooling – Van Wrap</title>
<link rel="stylesheet" href="https://fonts.googleapis.com/css2?family=Open+Sans:wght@600;800&display=swap">
<style>
  :root {
    --backdrop: #d2d2d2;
    --navy: #1a1f86;
    --sky: #33a6d7;
    --deep-sky: #0a7fd0;
    --ice: #85cae6;
    --frost: #f4f8fb;
    --sun: #f7c21a;
    --amber: #f78f20;
    --ember: #f37122;
    --tag-grey: #3a3a4a;
    --band: #2b2b2b;
  }
  * { box-sizing: border-box; margin: 0; padding: 0; }
  html, body {
    width: 1200px;
    height: 800px;
    overflow: hidden;
    background: var(--backdrop);
  }
  .canvas {
    position: relative;
    width: 1200px;
    height: 800px;
  }
  .wrap-panel {
    position: absolute;
    left: 60px;
    top: 160px;
    width: 1080px;
    height: 480px;
    border-radius: 28px;
    overflow: hidden;
    background:
      radial-gradient(ellipse 55% 70% at 100% 85%, var(--ember) 0%, var(--amber) 30%, rgba(247,194,26,0.85) 50%, rgba(247,194,26,0) 75%),
      radial-gradient(ellipse 60% 80% at 0% 0%, var(--deep-sky) 0%, var(--sky) 35%, rgba(133,202,230,0.6) 60%, rgba(133,202,230,0) 85%),
      linear-gradient(120deg, var(--sky) 0%, var(--ice) 30%, var(--frost) 55%, #fff7e0 75%, var(--sun) 100%);
  }
  .frost-spark {
    position: absolute;
    left: 30px;
    top: 280px;
    width: 140px;
    height: 140px;
    border-radius: 50%;
    background: radial-gradient(circle, rgba(255,255,255,0.75) 0%, rgba(255,255,255,0) 70%);
  }
  .sun-glow {
    position: absolute;
    right: 20px;
    top: 150px;
    width: 260px;
    height: 260px;
    border-radius: 50%;
    background: radial-gradient(circle, rgba(255,250,220,0.9) 0%, rgba(255,236,160,0.4) 40%, rgba(255,236,160,0) 70%);
  }
  .rocker-band {
    position: absolute;
    left: 0;
    right: 0;
    bottom: 70px;
    height: 22px;
    background: var(--band);
  }
  .brand {
    position: absolute;
    left: 470px;
    top: 92px;
    width: 560px;
    text-align: center;
    font-family: "Open Sans", sans-serif;
  }
  .brand-name {
    display: flex;
    align-items: center;
    justify-content: center;
    gap: 16px;
    font-weight: 600;
    font-size: 54px;
    line-height: 1.1;
    color: var(--navy);
  }
  .brand-dot {
    width: 22px;
    height: 22px;
    border-radius: 50%;
    background: var(--navy);
  }
  .brand-tagline {
    margin-top: 6px;
    font-weight: 600;
    font-size: 18px;
    letter-spacing: 1px;
    color: var(--tag-grey);
  }
  .contact {
    position: absolute;
    left: 470px;
    top: 232px;
    width: 560px;
    text-align: center;
    font-family: "Open Sans", sans-serif;
    color: var(--navy);
  }
  .contact-phone {
    font-weight: 800;
    font-size: 56px;
    letter-spacing: 4px;
    line-height: 1.1;
  }
  .contact-web {
    font-weight: 600;
    font-size: 32px;
    line-height: 1.3;
  }
</style>
</head>
<body>
  <main class="canvas">
    <section class="wrap-panel">
      <div class="frost-spark" role="img" aria-label="Frosty snowflake sparkle on the cool side"></div>
      <div class="sun-glow" role="img" aria-label="Warm sunburst glow on the hot side"></div>
      <div class="rocker-band"></div>

      <header class="brand">
        <h1 class="brand-name"><span class="brand-dot"></span>Brisk Flow</h1>
        <p class="brand-tagline">HEATING AND COOLING</p>
      </header>

      <div class="contact">
        <p class="contact-phone">416-502-3964</p>
        <p class="contact-web">brisk-flow.ca</p>
      </div>
    </section>
  </main>
</body>
</html>
```